New business card for UK roofing company

We are Brindmore Roofing and we need a business card design for our staff.

We offer the following services:

- New roofs
- General roof repairs
- Drone surveys
- Single ply roofing
- Steel cladding
- Asbestos removal
- Electronic leak detection

I have attached our logo. I have also attached example branding printed to our vans. The business card should fit in with the style of our branding.

The business card should have the following information;

Address:
Unit 17c Wendlecroft Farm
Wendlecroft Lane
Hatchington
CM4 9QD

Telephone: 020 7946 0372
24 Hour: 0800 612 4479

Email: ray@brindmoreroofing.example
Mobile: 07700981234
Name: Ray Tunstead
Website: www.brindmoreroofing.example

The business card will be printed in Spot UV, see here: https://www.kestaprint.example/business-cards/spot-uv/

If you need anymore info, please let me know,

```html
<!DOCTYPE html>
<html lang="en">
<head>
<meta charset="utf-8">
<title>Brindmore Roofing – Business Card</title>
<link rel="stylesheet" href="https://fonts.googleapis.com/css2?family=Montserrat:wght@400;600;700&display=swap">
<style>
  :root {
    --navy: #1d4f8f;
    --navy-deep: #173f74;
    --sky: #25b4e4;
    --ink: #4a4a4a;
    --paper: #ffffff;
    --card-black: #1c1c1e;
    --emboss: #2f2f32;
    --backdrop: #d9d9dc;
  }
  * { box-sizing: border-box; margin: 0; padding: 0; }
  html, body {
    width: 1200px; height: 716px; overflow: hidden;
    background: var(--backdrop);
    font-family: "Montserrat", sans-serif;
  }
  .sheet {
    position: relative; width: 1200px; height: 716px;
    display: flex; align-items: center; justify-content: center; gap: 40px;
  }
  .card {
    position: relative; width: 540px; height: 309px; overflow: hidden;
    box-shadow: 0 6px 18px rgba(0,0,0,0.18);
  }

  /* Back */
  .card--back {
    background: var(--card-black);
    border-bottom: 4px solid var(--navy);
    display: flex; align-items: center; justify-content: center; gap: 14px;
  }
  .back-mark {
    width: 40px; height: 40px; border-radius: 50%; background: var(--emboss);
  }
  .back-name {
    font-weight: 600; font-size: 32px; color: var(--emboss);
  }

  /* Front */
  .card--front { background: var(--paper); }
  .brand {
    position: absolute; top: 32px; right: 30px;
    display: flex; align-items: center; gap: 12px;
  }
  .brand-dot { width: 38px; height: 38px; border-radius: 50%; background: var(--sky); }
  .brand-name {
    font-weight: 600; font-size: 28px; color: var(--sky);
  }
  .rule {
    position: absolute; left: 30px; right: 30px; top: 92px;
    height: 1px; background: var(--sky);
  }
  .services {
    position: absolute; left: 30px; top: 104px; list-style: none;
    font-size: 11.5px; line-height: 16.5px; color: var(--ink);
  }
  .services li { position: relative; padding-left: 11px; }
  .services li::before {
    content: ""; position: absolute; left: 0; top: 5px;
    width: 6px; height: 6px; border-radius: 50%; background: var(--sky);
  }
  .person {
    position: absolute; right: 30px; top: 112px; text-align: right;
  }
  .person-name {
    font-weight: 700; font-size: 19px; letter-spacing: 1px; color: var(--navy-deep);
    text-transform: uppercase; margin-bottom: 8px;
  }
  .contacts { list-style: none; font-size: 11.5px; line-height: 17px; color: var(--ink); }
  .contacts li { display: flex; justify-content: flex-end; align-items: center; gap: 6px; }
  .contacts svg { width: 10px; height: 10px; fill: var(--navy); flex: none; }
  .hours { color: var(--sky); }
  .address-band {
    position: absolute; left: 0; right: 0; bottom: 0; height: 30px;
    background: linear-gradient(90deg, var(--navy-deep), var(--navy));
    border-top: 2px solid var(--sky);
    display: flex; align-items: center; gap: 7px; padding-left: 30px;
    color: var(--paper); font-size: 11.5px; letter-spacing: 0.2px;
  }
  .address-band svg { width: 9px; height: 12px; fill: var(--paper); }
</style>
</head>
<body>
<main class="sheet">

  <section class="card card--back" aria-label="Card back">
    <span class="back-mark"></span>
    <span class="back-name">Brindmore Roofing</span>
  </section>

  <section class="card card--front" aria-label="Card front">
    <div class="brand">
      <span class="brand-dot"></span>
      <span class="brand-name">Brindmore Roofing</span>
    </div>
    <div class="rule"></div>

    <ul class="services">
      <li>New roofs</li>
      <li>General roof repairs</li>
      <li>Drone surveys</li>
      <li>Single ply roofing</li>
      <li>Steel cladding</li>
      <li>Asbestos removal</li>
      <li>Electronic leak detection</li>
    </ul>

    <div class="person">
      <p class="person-name">Ray Tunstead</p>
      <ul class="contacts">
        <li><span>020 7946 0372</span>
          <svg viewBox="0 0 10 10"><path d="M1 4c0-2 8-2 8 0v1H7V4H3v1H1z M2 6h6l1 3H1z"/></svg></li>
        <li><span>0800 612 4479 (<span class="hours">24 Hour</span>)</span>
          <svg viewBox="0 0 10 10"><path d="M2 1l2 2-1 1c1 2 2 3 3 3l1-1 2 2-1 2C4 10 0 6 0 2z"/></svg></li>
        <li><span>07700981234</span>
          <svg viewBox="0 0 10 10"><path d="M3 0h4a1 1 0 0 1 1 1v8a1 1 0 0 1-1 1H3a1 1 0 0 1-1-1V1a1 1 0 0 1 1-1zm0 1.5v6h4v-6z"/></svg></li>
        <li><span>ray@brindmoreroofing.example</span>
          <svg viewBox="0 0 10 10"><path d="M0 2h10v6H0zm1 1v.3l4 2.5 4-2.5V3zm0 1.5V7h8V4.5L5 7z"/></svg></li>
        <li><span>www.brindmoreroofing.example</span>
          <svg viewBox="0 0 10 10"><path d="M5 0a5 5 0 1 0 0 10A5 5 0 0 0 5 0zm0 1a4 4 0 0 1 0 8 4 4 0 0 1 0-8zM1.5 4.5h7v1h-7zM4.5 1h1v8h-1z"/></svg></li>
      </ul>
    </div>

    <footer class="address-band">
      <svg viewBox="0 0 9 12"><path d="M4.5 0A4.5 4.5 0 0 1 9 4.5C9 7.5 4.5 12 4.5 12S0 7.5 0 4.5A4.5 4.5 0 0 1 4.5 0zm0 2.5a2 2 0 1 0 0 4 2 2 0 0 0 0-4z"/></svg>
      <span>Unit 17c Wendlecroft Farm Wendlecroft Lane Hatchington CM4 9QD</span>
    </footer>
  </section>

</main>
</body>
</html>
```